Gourmet food made with love and care in my country kitchen

I'd like a business card designed for my small home-based food business. I have made labelling in federation blue for my food products (Labneh cheese, spicy pumpkin chutney, dukkah, caramelised onion jam, yo-Yo biscuits, chocolate mud cake etc) and have navy and white checked surrounds/borders on my brochures so would like to stick to these country colours.
Target Market(s)
Foodies who love gourmet delicacies. Everyone who enjoys a picnic that they don't have to prepare themselves.
Industry/Entity Type
Business
Contact Information for Business Card
Larkhollow Pantry
42 Tindale's Lane
Brimsworth Qld 4829
Phone Viv 07 48216597 or 0412386951
- Harrington

```html
<!DOCTYPE html>
<html lang="en">
<head>
<meta charset="utf-8">
<title>Larkhollow Pantry</title>
<link rel="stylesheet" href="https://fonts.googleapis.com/css2?family=Dancing+Script:wght@500;700&family=Arimo:wght@400&display=swap">
<style>
  :root {
    --federation-blue: #1a4de6;
    --sky-blue: #8bc1f1;
    --stripe-blue: #1747e0;
    --white: #ffffff;
    --field-green: #5fae3a;
    --sky-light: #cfe6f5;
    --script: "Dancing Script", cursive;
    --sans: "Arimo", Arial, sans-serif;
  }
  html, body { margin: 0; padding: 0; overflow: hidden; background: #ffffff; }
  .card {
    position: relative;
    width: 972px;
    height: 1200px;
    background: var(--sky-blue);
    overflow: hidden;
  }
  .top-band {
    position: absolute; left: 0; top: 0;
    width: 972px; height: 519px;
    background: var(--federation-blue);
  }
  .brand-name {
    position: absolute;
    margin: 0;
    color: var(--white);
    font-family: var(--script);
    font-weight: 500;
    line-height: 1;
  }
  .brand-name span { display: block; }
  .brand-name--hero { left: 52px; top: 238px; font-size: 118px; }
  .brand-name--hero span + span { margin-left: 66px; margin-top: 8px; }
  .brand-name--panel { left: 574px; top: 618px; font-size: 84px; }
  .brand-name--panel span + span { margin-left: 52px; margin-top: 6px; }
  .services {
    position: absolute; left: 0; top: 534px;
    width: 972px;
    display: flex; justify-content: center; gap: 40px;
    padding-left: 0;
    margin: 0; list-style: none;
    color: var(--white);
    font-family: var(--script);
    font-weight: 700;
    font-size: 28px;
  }
  .services li { white-space: nowrap; }
  .photo {
    position: absolute; left: 0; top: 600px;
    width: 533px; height: 600px;
    background: linear-gradient(180deg, var(--sky-light) 0%, #b9d9ee 45%, #7fbf52 58%, var(--field-green) 75%, #3f8a2a 100%);
  }
  .photo-stripe {
    position: absolute; left: 533px; top: 600px;
    width: 13px; height: 600px;
    background: var(--stripe-blue);
  }
  .promise {
    position: absolute; left: 44px; top: 1030px;
    margin: 0;
    color: var(--white);
    font-family: var(--script);
    font-weight: 700;
    font-size: 20px;
    line-height: 35px;
  }
  .contact {
    position: absolute; right: 17px; top: 970px;
    margin: 0;
    text-align: right;
    color: var(--white);
    font-family: var(--sans);
    font-style: normal;
    font-size: 26px;
    line-height: 29px;
    letter-spacing: -0.5px;
  }
  .contact .accent { color: var(--federation-blue); }
  .contact .social::before {
    content: "";
    display: inline-block;
    width: 24px; height: 24px;
    margin-right: 7px;
    vertical-align: -3px;
    background: var(--federation-blue);
    border-radius: 3px;
  }
</style>
</head>
<body>
<main class="card">
  <header class="top-band">
    <h1 class="brand-name brand-name--hero"><span>Larkhollow</span><span>Pantry</span></h1>
  </header>

  <ul class="services">
    <li>Gourmet market food</li>
    <li>Vintage Picnic Hampers</li>
    <li>Cooking Classes</li>
  </ul>

  <div class="photo" role="img" aria-label="Photograph of tall gum trees beside a white rail fence and a dirt track, with green cane fields and distant hills under a pale sky"></div>
  <div class="photo-stripe"></div>

  <p class="promise">Gourmet food made in my country kitchen,<br>using fresh ingredients, for your<br>enjoyment and convenience.<br>Viv Harlow</p>

  <p class="brand-name brand-name--panel"><span>Larkhollow</span><span>Pantry</span></p>

  <address class="contact">
    <span class="accent">Viv</span><br>
    0748 216597 <span class="accent">Or</span> 041 2386951<br>
    42 Tindale's Lane<br>
    Mt Orrin Via Brimsworth<br>
    <span class="social">Larkhollow Pantry</span><br>
    <span class="accent">larkhollowpantry@pantrymail.com</span>
  </address>
</main>
</body>
</html>
```